KELPMARROW, LLC needs a hybrid app to evaluate and develop athletes

KELPMARROW, LLC needs initial hybrid mobile app and website holding page. KELPMARROW, LLC allows athletes to develop their skills (soccer is initial sport) for free. Receive daily/weekly reminders. Access training videos. Earn points to "upgrade" their soccer profile in "app soccer store". See their points/rankings compared to all app users. Progress streak. This free app (for athletes) will communicate to paid app (coaches) in the future. We would like to see designs use the color blue. The design will communicate health and wellness.

```html
<!DOCTYPE html>
<html lang="en">
<head>
<meta charset="utf-8">
<title>KELPMARROW – App Screens</title>
<link href="https://fonts.googleapis.com/css2?family=Work+Sans:wght@300;400;500&display=swap" rel="stylesheet">
<style>
  :root{
    --stage:#02060f;
    --white:#ffffff;
    --navy-top:#0a1f52;
    --navy-mid:#15398a;
    --grass:#1c4760;
    --field-input:#1a3f86;
    --field-border:#6f8fc4;
    --login-btn:#8cb2da;
    --create-btn:#0a6cc8;
    --icon-square:#2f6fc0;
    --divider:rgba(190,205,235,.45);
    --progress:#3cc23c;
    --nav:#0a58a8;
    --ring:#f6b31c;
    --grey-base:#aab3c7;
    --grey-patch:#6b7589;
    --green:#2e9a5c;
    --teal:#2fa597;
    --purple:#7a3fb0;
    --red:#b23b32;
    --orange:#f6a623;
    --nav-green:#3cc23c;
  }
  *{box-sizing:border-box;margin:0;padding:0}
  html,body{width:1043px;height:1200px;overflow:hidden}
  body{background:var(--stage);font-family:"Work Sans",sans-serif;color:var(--white);position:relative}

  .screen-title{position:absolute;top:126px;font-size:21px;font-weight:400;letter-spacing:.5px;text-align:center;width:421px}
  .screen-title--login{left:58px}
  .screen-title--training{left:563px;width:423px}

  .screen{position:absolute;top:174px;overflow:hidden}
  .screen__photo{position:absolute;inset:0}

  /* Login */
  .login{left:58px;width:421px;height:658px}
  .login .screen__photo{background:linear-gradient(180deg,var(--navy-top) 0%,#11307a 35%,var(--navy-mid) 60%,var(--grass) 78%,#173a68 100%)}
  .brand{position:absolute;left:0;right:0;text-align:center;font-weight:300;letter-spacing:1.5px}
  .login .brand{top:58px;font-size:26px}
  .brand-rule{position:absolute;left:50%;height:1px;background:var(--white);transform:translateX(-50%)}
  .login .brand-rule{top:99px;width:166px}
  .athlete-heading{position:absolute;top:158px;left:107px;display:flex;align-items:center;gap:13px}
  .athlete-heading__icon{width:33px;height:29px;background:var(--icon-square);display:flex;align-items:center;justify-content:center}
  .athlete-heading__text{font-size:20px;font-weight:400;letter-spacing:1px}
  .field,.btn{position:absolute;left:83px;width:256px;font-size:11.5px;letter-spacing:1.2px;font-weight:500}
  .field{height:34px;background:var(--field-input);border:1px solid var(--field-border);padding-left:11px;display:flex;align-items:center}
  .field--username{top:225px}
  .field--password{top:269px}
  .btn{display:flex;align-items:center;justify-content:center}
  .btn--login{top:315px;height:34px;background:var(--login-btn);color:#eef4fb}
  .btn--create{top:447px;height:39px;background:var(--create-btn);font-size:12.5px}

  /* Training */
  .training{left:563px;width:423px;height:879px}
  .training .screen__photo{background:radial-gradient(ellipse 60% 35% at 55% 48%,#1f4a98 0%,rgba(31,74,152,0) 100%),linear-gradient(180deg,var(--navy-top) 0%,#123481 40%,#153a86 70%,#1d4a72 92%,#1b4470 100%)}
  .training .brand{top:36px;font-size:16px;font-weight:400;letter-spacing:1.5px}
  .training .brand-rule{top:70px;width:110px}
  .challenge{position:absolute;top:94px;left:0;right:0;display:flex;justify-content:center;align-items:center;gap:8px;font-size:13px;letter-spacing:1.3px;font-weight:500}
  .challenge svg{width:27px;height:27px}
  .challenge span{margin-left:4px}

  .week-grid{position:absolute;top:146px;left:10px;width:404px}
  .week-row{position:relative;height:126px;display:grid;grid-template-columns:repeat(4,1fr)}
  .week-row::after{content:"";position:absolute;left:11px;right:11px;bottom:0;height:1px;background:var(--divider)}
  .week-row__progress{position:absolute;right:22px;bottom:-1px;width:51px;height:4px;border-radius:2px;background:var(--progress);z-index:1}
  .week{display:flex;flex-direction:column;align-items:center;padding-top:19px}
  .week svg{width:64px;height:64px}
  .week__label{margin-top:7px;font-size:13px;line-height:16px;font-weight:500}

  .ball-ring{fill:none;stroke:var(--ring);stroke-width:6}
  .ball-base{fill:var(--ball-base,#fff);stroke:var(--ball-patch);stroke-width:3}
  .ball-patch{fill:var(--ball-patch)}
  .ball-seam{stroke:var(--ball-patch);stroke-width:3}
  .is-locked{--ball-base:var(--grey-base);--ball-patch:var(--grey-patch)}
  .is-locked .ball-ring{stroke:none}
  .is-locked .ball-base{stroke:none}
  .is-green{--ball-patch:var(--green)}
  .is-teal{--ball-patch:var(--teal)}
  .is-purple{--ball-patch:var(--purple)}
  .is-red{--ball-patch:var(--red)}
  .is-orange{--ball-patch:var(--orange)}
  .is-nav{--ball-patch:var(--nav-green)}
  .is-nav .ball-ring,.challenge .ball-ring{stroke:none}

  .tab-bar{position:absolute;left:0;right:0;bottom:0;height:76px;background:var(--nav);display:grid;grid-template-columns:repeat(4,1fr);align-items:center;justify-items:center}
  .tab-bar svg{display:block}
</style>
</head>
<body>

<svg width="0" height="0" style="position:absolute" aria-hidden="true">
  <defs>
    <clipPath id="ball-clip"><circle r="42"/></clipPath>
    <symbol id="ball" viewBox="-52 -52 104 104">
      <circle class="ball-ring" r="48"/>
      <circle class="ball-base" r="42"/>
      <g clip-path="url(#ball-clip)">
        <g class="ball-seam">
          <line x1="0" y1="-14" x2="0" y2="-26"/>
          <line x1="13.3" y1="-4.3" x2="24.7" y2="-8"/>
          <line x1="8.2" y1="11.3" x2="15.3" y2="21"/>
          <line x1="-8.2" y1="11.3" x2="-15.3" y2="21"/>
          <line x1="-13.3" y1="-4.3" x2="-24.7" y2="-8"/>
        </g>
        <polygon class="ball-patch" points="0,-14 13.3,-4.3 8.2,11.3 -8.2,11.3 -13.3,-4.3"/>
        <g class="ball-patch">
          <polygon transform="rotate(36) translate(0,-40) rotate(180)" points="0,-13 12.4,-4 7.6,10.5 -7.6,10.5 -12.4,-4"/>
          <polygon transform="rotate(108) translate(0,-40) rotate(180)" points="0,-13 12.4,-4 7.6,10.5 -7.6,10.5 -12.4,-4"/>
          <polygon transform="rotate(180) translate(0,-40) rotate(180)" points="0,-13 12.4,-4 7.6,10.5 -7.6,10.5 -12.4,-4"/>
          <polygon transform="rotate(252) translate(0,-40) rotate(180)" points="0,-13 12.4,-4 7.6,10.5 -7.6,10.5 -12.4,-4"/>
          <polygon transform="rotate(324) translate(0,-40) rotate(180)" points="0,-13 12.4,-4 7.6,10.5 -7.6,10.5 -12.4,-4"/>
        </g>
      </g>
    </symbol>
  </defs>
</svg>

<h2 class="screen-title screen-title--login">Login page</h2>
<h2 class="screen-title screen-title--training">Training page</h2>

<!-- Login screen -->
<section class="screen login">
  <div class="screen__photo" role="img" aria-label="Night stadium pitch with a soccer ball on the grass, tinted blue"></div>
  <div class="brand">KELPMARROW</div>
  <div class="brand-rule"></div>
  <div class="athlete-heading">
    <div class="athlete-heading__icon">
      <svg width="14" height="15" viewBox="0 0 14 15"><circle cx="7" cy="4" r="3.6" fill="#fff"/><path d="M0.5 15 V12 Q0.5 8.5 4 8.5 H10 Q13.5 8.5 13.5 12 V15 Z" fill="#fff"/></svg>
    </div>
    <div class="athlete-heading__text">ATHLETE LOGIN</div>
  </div>
  <div class="field field--username">USERNAME</div>
  <div class="field field--password">PASSWORD</div>
  <div class="btn btn--login">LOG IN</div>
  <div class="btn btn--create">CREATE ACCOUNT</div>
</section>

<!-- Training screen -->
<section class="screen training">
  <div class="screen__photo" role="img" aria-label="Large soccer ball resting on grass, faint blue-tinted backdrop"></div>
  <div class="brand">KELPMARROW</div>
  <div class="brand-rule"></div>
  <div class="challenge">
    <svg class="is-orange"><use href="#ball"/></svg>
    <span>WEEKLY TRAINING CHALLENGE</span>
  </div>

  <div class="week-grid">
    <div class="week-row">
      <div class="week is-locked"><svg><use href="#ball"/></svg><span class="week__label">W1</span></div>
      <div class="week is-locked"><svg><use href="#ball"/></svg><span class="week__label">W2</span></div>
      <div class="week is-locked"><svg><use href="#ball"/></svg><span class="week__label">W3</span></div>
      <div class="week is-locked"><svg><use href="#ball"/></svg><span class="week__label">W4</span></div>
    </div>
    <div class="week-row">
      <div class="week is-locked"><svg><use href="#ball"/></svg><span class="week__label">W5</span></div>
      <div class="week is-green"><svg><use href="#ball"/></svg><span class="week__label">W6</span></div>
      <div class="week is-teal"><svg><use href="#ball"/></svg><span class="week__label">W7</span></div>
      <div class="week is-purple"><svg><use href="#ball"/></svg><span class="week__label">W8</span></div>
    </div>
    <div class="week-row">
      <div class="week is-red"><svg><use href="#ball"/></svg><span class="week__label">W9</span></div>
      <div class="week is-red"><svg><use href="#ball"/></svg><span class="week__label">W10</span></div>
      <div class="week is-locked"><svg><use href="#ball"/></svg><span class="week__label">W11</span></div>
      <div class="week is-teal"><svg><use href="#ball"/></svg><span class="week__label">W12</span></div>
    </div>
    <div class="week-row">
      <div class="week is-teal"><svg><use href="#ball"/></svg><span class="week__label">W13</span></div>
      <div class="week is-purple"><svg><use href="#ball"/></svg><span class="week__label">W14</span></div>
      <div class="week is-purple"><svg><use href="#ball"/></svg><span class="week__label">W15</span></div>
      <div class="week is-locked"><svg><use href="#ball"/></svg><span class="week__label">W16</span></div>
      <div class="week-row__progress"></div>
    </div>
    <div class="week-row">
      <div class="week is-locked"><svg><use href="#ball"/></svg><span class="week__label">W17</span></div>
      <div class="week is-locked"><svg><use href="#ball"/></svg><span class="week__label">W18</span></div>
      <div class="week is-locked"><svg><use href="#ball"/></svg><span class="week__label">W19</span></div>
      <div class="week is-locked"><svg><use href="#ball"/></svg><span class="week__label">W20</span></div>
    </div>
  </div>

  <nav class="tab-bar">
    <svg class="is-nav" width="42" height="42"><use href="#ball"/></svg>
    <svg width="24" height="28" viewBox="0 0 24 28" aria-label="Profile"><circle cx="12" cy="7" r="6" fill="#fff"/><path d="M1 28 V21 Q1 15 7 15 H17 Q23 15 23 21 V28 Z" fill="#fff"/></svg>
    <svg width="30" height="34" viewBox="0 0 30 34" aria-label="Team"><path d="M15 1 L28 6 V15 Q28 27 15 33 Q2 27 2 15 V6 Z" fill="none" stroke="#fff" stroke-width="3"/><path d="M15 3 V31 Q4 26 4 15 V7.5 Z" fill="#fff"/></svg>
    <svg width="44" height="24" viewBox="0 0 44 24" aria-label="Gear"><path d="M2 18 L4 9 Q7 7 10 8 L14 3 Q16 1 18 3 L23 9 Q33 11 40 13 Q43 14 42 18 Z" fill="#fff"/><g stroke="#0a58a8" stroke-width="2"><line x1="14" y1="5" x2="19" y2="11"/><line x1="18" y1="3" x2="24" y2="11"/><line x1="10" y1="9" x2="15" y2="14"/></g><g fill="#fff"><rect x="4" y="20" width="3" height="3"/><rect x="10" y="20" width="3" height="3"/><rect x="16" y="20" width="3" height="3"/><rect x="27" y="20" width="3" height="3"/><rect x="33" y="20" width="3" height="3"/></g></svg>
  </nav>
</section>

</body>
</html>
```